PawQuarry Banner contest an ecommerce site for veterinarians

We need banners for our ecommerce site. Our site is a webstore that veterinarians can use to allow their clients to purchase items from them. Each month we have a different theme for our banners. I am looking for banners for January and February and with a refresh coming to our site could be looking at a dozen over the next year. I may potentially choose from multiple designers and increase the payment or will choose one designer for both months .

For January our theme is winter fun. We will be running a contest were people can submit a picture of their pet to our Chatterloop page enjoying the snow or keeping warm. they have a chance to win one of 5 $50 gift certificates to pawquarry. The banner should have a dog and cat and a separate one with just a cat. We will need a French and English banner. We will provide the French translation once the winner has been selected.

For February our theme is dental health. The banner should have a dog and cat and a separate one with just a cat. We will need a French and English banner. We will provide the French translation once the winner has been selected.

Target Market(s)

pet owners

Industry/Entity Type

Veterinary

Colors

Designer to choose colors to be used in the design.

Requirements
Must have
• dimensions for PQ Banner are: 710px x 280px
Nice to have
• I have attached our logo and some screen shoots of our site so you can get a feel of what it look like. you could also go to www.pawquarry.ca and see what the sign in page looks like
Should not have
• images of pet food

```html
<!DOCTYPE html>
<html lang="en">
<head>
<meta charset="utf-8">
<title>PawQuarry – Pet Dental Health Month Banner</title>
<link href="https://fonts.googleapis.com/css2?family=Roboto:wght@500;700&display=swap" rel="stylesheet">
<style>
  :root {
    --brand-red: #c1262d;
    --paper: #f4f4f3;
    --paper-edge: #e4e4e2;
    --white: #ffffff;
    --dog-tan: #c08c52;
    --dog-light: #d7a86e;
    --dog-dark: #5a3a1c;
    --cat-grey: #8f9398;
    --cat-grey-light: #b5b8bc;
    --cat-white: #f6f6f6;
  }
  html, body {
    margin: 0;
    padding: 0;
    overflow: hidden;
  }
  .banner {
    position: relative;
    width: 1200px;
    height: 473px;
    overflow: hidden;
    background: radial-gradient(ellipse at 35% 45%, var(--paper) 0%, var(--paper) 55%, var(--paper-edge) 100%);
    font-family: "Roboto", Arial, sans-serif;
  }
  .month-tag {
    position: absolute;
    left: 42px;
    top: 68px;
    height: 37px;
    padding: 0 10px;
    background: var(--brand-red);
    color: var(--white);
    font-size: 29px;
    font-weight: 500;
    line-height: 37px;
    white-space: nowrap;
    letter-spacing: -0.2px;
  }
  .headline {
    position: absolute;
    left: 48px;
    top: 134px;
    margin: 0;
    color: var(--brand-red);
    font-size: 55px;
    font-weight: 500;
    line-height: 64px;
    letter-spacing: -0.3px;
  }
  .brand {
    position: absolute;
    left: 50px;
    top: 380px;
    display: flex;
    align-items: center;
    gap: 10px;
    color: var(--brand-red);
    font-size: 36px;
    font-weight: 700;
    line-height: 1;
  }
  .brand-dot {
    width: 16px;
    height: 16px;
    border-radius: 50%;
    background: var(--brand-red);
  }
  .pet-photo {
    position: absolute;
    top: 0;
    left: 0;
    width: 1200px;
    height: 473px;
  }
</style>
</head>
<body>
  <div class="banner">
    <div class="month-tag">February is National Pet Dental Health Month</div>
    <h1 class="headline">How much do you<br>know about your pet’s<br>dental health?</h1>
    <div class="brand"><span class="brand-dot"></span>pawquarry</div>

    <svg class="pet-photo" viewBox="0 0 1200 473" role="img" aria-label="Photo of a tan dog in profile, mouth open, wearing a chain collar">
      <defs>
        <radialGradient id="dog-tone" cx="0.55" cy="0.35" r="0.8">
          <stop offset="0" stop-color="var(--dog-light)"/>
          <stop offset="0.55" stop-color="var(--dog-tan)"/>
          <stop offset="1" stop-color="var(--dog-dark)"/>
        </radialGradient>
        <filter id="soft-dog" x="-20%" y="-20%" width="140%" height="140%">
          <feGaussianBlur stdDeviation="6"/>
        </filter>
      </defs>
      <path filter="url(#soft-dog)" fill="url(#dog-tone)"
            d="M712 215 C740 185 800 170 860 180 C905 190 935 220 945 270 L945 473 L770 473 C775 430 760 360 730 330 C705 310 695 260 712 215 Z"/>
    </svg>

    <svg class="pet-photo" viewBox="0 0 1200 473" role="img" aria-label="Photo of a grey and white cat looking toward the viewer">
      <defs>
        <linearGradient id="cat-tone" x1="0" y1="0" x2="0" y2="1">
          <stop offset="0" stop-color="var(--cat-grey)"/>
          <stop offset="0.4" stop-color="var(--cat-grey-light)"/>
          <stop offset="0.62" stop-color="var(--cat-white)"/>
          <stop offset="1" stop-color="var(--white)"/>
        </linearGradient>
        <filter id="soft-cat" x="-20%" y="-20%" width="140%" height="140%">
          <feGaussianBlur stdDeviation="8"/>
        </filter>
      </defs>
      <path filter="url(#soft-cat)" fill="url(#cat-tone)"
            d="M830 60 C860 30 900 20 940 30 C1000 10 1080 -10 1140 0 L1210 0 L1210 480 L900 480 C880 430 840 380 820 320 C800 250 800 150 830 60 Z"/>
    </svg>
  </div>
</body>
</html>
```